Kick Ass, Edgy, Fun, E commerce Embroidery Company Business Card

Sleek and edgy business card layout. main logo on front with business description (Custom Embroidery, the file is submitted is supposed to look like stitching)
Name, address, phone numbers, social icons (Facebook and Instagram) on back. The card will be black plastic and the front main logo will be printed Spot UV.

Target Market(s)

Small Business Owners

Contact Information for Business Card

Focused, not cluttered and sleek. Modern looking.

Font styles to use
Other font styles liked:
• Very clean and elegant

Colors
acd136

Requirements
Must have
• Custom Embroidery

our Tagline: Every Logo Has A Story - Thread Yours
Nice to have
• Social Icons for Facebook and Instagram
Should not have
• Too much visual noise

```html
<!DOCTYPE html>
<html lang="en">
<head>
<meta charset="utf-8">
<title>StitchRiot Business Card</title>
<link rel="stylesheet" href="https://fonts.googleapis.com/css2?family=Archivo+Black&family=Raleway:wght@500;800&family=Saira+Condensed:wght@400&display=swap">
<style>
  :root {
    --backdrop: #1c2d3e;
    --card: #000000;
    --lime: #acd136;
    --white: #ffffff;
  }
  * { margin: 0; padding: 0; box-sizing: border-box; }
  html, body {
    width: 1200px; height: 1200px; overflow: hidden;
    background: var(--backdrop);
  }
  .canvas { position: relative; width: 1200px; height: 1200px; }
  .card {
    position: absolute; left: 281px; width: 639px; height: 393px;
    background: var(--card); border-radius: 19px; overflow: hidden;
  }
  .card--front { top: 150px; }
  .card--back { top: 656px; }

  .brand {
    position: absolute; left: 124px; top: 70px;
    display: flex; align-items: center; gap: 24px;
  }
  .brand__dot {
    width: 100px; height: 100px; border-radius: 50%;
    background: var(--white); flex: none;
  }
  .brand__name {
    font-family: "Archivo Black", sans-serif;
    font-size: 62px; line-height: 56px; color: var(--white);
    text-transform: uppercase;
  }
  .service {
    position: absolute; left: 0; right: 0; top: 236px;
    text-align: center;
    font-family: "Archivo Black", sans-serif;
    font-size: 42px; line-height: 54px; letter-spacing: 3px;
    color: var(--lime); text-transform: uppercase;
  }

  .company {
    position: absolute; left: 0; right: 0; top: 44px;
    text-align: center;
    font-family: "Raleway", sans-serif; font-weight: 500;
    font-size: 46px; line-height: 56px; color: var(--lime);
  }
  .contact {
    position: absolute; left: 0; right: 0; top: 102px;
    text-align: center;
    font-family: "Saira Condensed", sans-serif; font-weight: 400;
    font-size: 27px; line-height: 34px; color: var(--white);
    letter-spacing: 0.3px;
  }
  .contact__address { margin-bottom: 30px; }
  .social {
    position: absolute; left: 0; right: 0; top: 278px;
    display: flex; justify-content: center; gap: 20px;
  }
  .social__icon {
    width: 32px; height: 32px; border-radius: 7px;
    border: 3px solid var(--white);
  }
  .social__icon--filled { background: var(--white); }
  .tagline-band {
    position: absolute; left: 0; right: 0; bottom: 0; height: 64px;
    background: var(--lime);
    display: flex; align-items: center; justify-content: center;
  }
  .tagline {
    font-family: "Raleway", sans-serif; font-weight: 800;
    font-size: 32px; color: var(--card); letter-spacing: -0.5px;
  }
</style>
</head>
<body>
<div class="canvas">
  <section class="card card--front">
    <div class="brand">
      <span class="brand__dot"></span>
      <span class="brand__name">Stitch<br>Riot</span>
    </div>
    <p class="service">Custom<br>Embroidery</p>
  </section>

  <section class="card card--back">
    <h1 class="company">StitchRiot Inc</h1>
    <div class="contact">
      <p class="contact__address">4471 Granite Ridge Way Ste 5 Lakewood, CO 80226</p>
      <p>1-800-555-0192</p>
      <p>info@StitchRiot.com</p>
      <p>StitchRiot.com</p>
    </div>
    <div class="social">
      <span class="social__icon"></span>
      <span class="social__icon social__icon--filled"></span>
    </div>
    <div class="tagline-band">
      <p class="tagline">Every Mark Tells A Tale -Stitch Yours</p>
    </div>
  </section>
</div>
</body>
</html>
```